Website for company called VORENTbio

We need a website for our new company called VORENTbio which developed a platform/technology to identify antigen-specific T cells (immune cells) which can be used for cancer therapy, autoimmunity, etc.

The platform is called VORENT and is rapid, versatile, unbiased, and inexpensive.

We have a semi-final logo although we are not completely set on color and font of text (attached).

Target Market(s)

Our target audience at the moment would be potential investors and VCs. We eventually are interested in getting attention from scientists and cell/immunotherapy companies.

Industry/Entity Type

Healthcare/Technology

Coding

Coded - Design and coding required

Number of Pages Required

1 page

Colors
0094D4
00A9DD
6FCCEA
C7EBF8
E9F6FB
00AB8E
00BBA5
67D7C9
C6EFE9
E9F9F6
E54698
E96AAD
F1A4CE
F9D9EA
FCEFF6
A7469A
B969AE
D3A5CF
EDDBEB
F8F0F9
6B429C
8869AF
B7A5CE
E3DAEB
F3F0F8

Requirements
Must have
• Landing page about the company, About us page, Technology page (could be merged with company landing page), Contact us page

```html
<!DOCTYPE html>
<html lang="en">
<head>
<meta charset="utf-8">
<title>VORENTbio — Redefining T Cell Discovery</title>
<link href="https://fonts.googleapis.com/css2?family=Lexend+Deca:wght@400;500;600&family=Poppins:wght@400;500;600&display=swap" rel="stylesheet">
<style>
:root{
  --blue:#0094D4;
  --blue-2:#00A9DD;
  --blue-soft:#C7EBF8;
  --blue-pale:#E9F6FB;
  --teal:#00AB8E;
  --teal-2:#00BBA5;
  --teal-soft:#67D7C9;
  --teal-pale:#E9F9F6;
  --navy:#1d3140;
  --footer:#13202c;
  --ink:#111820;
  --text:#4a5560;
  --muted:#7a858f;
  --white:#ffffff;
  --star:#f5a623;
}
*{box-sizing:border-box;margin:0;padding:0}
html,body{width:1200px;height:4481px;overflow:hidden}
body{position:relative;background:var(--white);font-family:"Poppins",sans-serif;color:var(--text);font-size:13px;line-height:1.6}
h1,h2,h3,h4,.brand,.stat-num{font-family:"Lexend Deca",sans-serif;color:var(--ink);font-weight:500}
.abs{position:absolute}
.eyebrow{font-family:"Lexend Deca",sans-serif;font-size:15px;letter-spacing:2.5px;color:var(--blue);font-weight:500;text-transform:uppercase}
.dash{display:flex;gap:5px;margin-top:10px}
.dash span{width:14px;height:2px;background:var(--blue)}
.center{text-align:center}
.center .dash{justify-content:center}
.btn{display:inline-flex;align-items:center;justify-content:center;border-radius:4px;font-size:13px;font-weight:500;height:36px;padding:0 20px}
.btn-blue{background:var(--blue);color:#fff}
.ph{border-radius:0}

/* header */
.hero-bg{left:0;top:0;width:1200px;height:1060px;background:linear-gradient(180deg,#fff 0%,#f3fafd 40%,#eef8fb 100%)}
.brand{display:flex;align-items:center;gap:8px;font-size:25px;font-weight:500;color:var(--ink)}
.brand-dot{width:22px;height:22px;border-radius:50%;background:var(--ink)}
.nav{left:350px;top:45px;display:flex;gap:38px;font-size:12px;color:var(--ink)}
.login{left:860px;top:36px;width:136px;height:36px;border-radius:18px;background:#fff;color:var(--ink);font-size:13px;font-weight:500;display:flex;align-items:center;justify-content:center;box-shadow:0 2px 8px rgba(0,0,0,.08)}
.contact-btn{left:1004px;top:36px;width:132px;height:36px;border-radius:18px;background:var(--blue);color:#fff;font-size:13px;font-weight:500;display:flex;align-items:center;justify-content:center}
.hero-img{left:569px;top:0;width:631px;height:530px;clip-path:polygon(32% 0,100% 0,100% 62%,62% 100%,3% 100%,0 62%,12% 28%);background:linear-gradient(135deg,#cfe6ee 0%,#6fb6cc 35%,#2a7e9a 70%,#1a5f78 100%)}
.hero h1{left:139px;top:148px;width:520px;font-size:38px;line-height:50px;font-weight:600}
.hero p{left:139px;top:312px;width:400px;font-size:12.5px;line-height:23px;color:var(--ink)}
.hero-btns{left:139px;top:410px;display:flex;gap:14px}
.pill{height:37px;border-radius:19px;font-size:12.5px;font-weight:500;display:flex;align-items:center;justify-content:center}
.pill-blue{width:134px;background:var(--blue);color:#fff}
.pill-line{width:154px;border:1.5px solid var(--blue);color:var(--ink);background:#fff}
.stats-bar{left:103px;top:527px;width:991px;height:84px;border-radius:42px;background:var(--teal);display:flex;align-items:center;color:#fff}
.stats-bar .item{flex:1;display:flex;align-items:center;justify-content:center;gap:14px;font-size:14px}
.stats-bar .item+.item{border-left:1px solid rgba(255,255,255,.5)}
.stats-bar .stat-num{color:#fff;font-size:32px;font-weight:500}

/* platform */
.platform-head{left:0;top:700px;width:1200px}
.platform-head h2{font-size:31px;margin-top:8px}
.feature{width:280px;height:205px;background:#fff;border-radius:6px;box-shadow:0 6px 24px rgba(20,60,90,.10);padding:64px 34px 0}
.feature h3{font-size:15px;font-weight:500;margin-bottom:16px}
.feature p{font-size:12px;line-height:22px;color:var(--text)}
.f-icon{width:62px;height:62px;border-radius:50%;display:flex;align-items:center;justify-content:center;border:5px solid #fff;box-shadow:0 4px 14px rgba(0,0,0,.12)}

/* about */
.about-accent{left:111px;top:1344px;width:66px;height:156px;background:var(--navy)}
.about-img{left:141px;top:1148px;width:403px;height:332px;background:linear-gradient(135deg,#a9c4d0,#5f8ea0 50%,#2e5566)}
.badge{left:500px;top:1352px;width:86px;height:86px;border-radius:50%;background:#fff;border:2px dashed #9aa6ae}
.about-text{left:600px;top:1140px;width:470px}
.about-text h2{font-size:31px;margin-top:4px}
.about-text p{font-size:12.5px;line-height:20.5px;margin-top:14px}
.link-blue{color:var(--blue);font-size:13px;font-weight:500}

/* stats band */
.stats-band{left:0;top:1600px;width:1200px;height:257px;background:linear-gradient(135deg,#0aa98d,#18b8a0 55%,#0aa98d)}
.notch{left:572px;top:1856px;width:0;height:0;border-left:28px solid transparent;border-right:28px solid transparent;border-top:24px solid #0aa98d}
.band-stats{left:80px;top:1680px;width:1040px;display:flex;color:#fff}
.band-stats .item{flex:1;text-align:center;padding:10px 0}
.band-stats .item+.item{border-left:1px solid rgba(255,255,255,.35)}
.band-stats .stat-num{color:#fff;font-size:42px;line-height:50px}
.band-stats span{font-size:16px}
.cross{width:80px;height:80px}

/* team */
.team-text{left:131px;top:1976px;width:470px}
.team-text h2{font-size:31px;margin-top:4px}
.team-text p{font-size:12.5px;line-height:20.5px;margin-top:12px;color:var(--text)}
.check{display:flex;align-items:center;gap:8px;font-size:12.5px;color:var(--ink)}
.check i{width:20px;height:20px;border-radius:50%;background:var(--teal);display:inline-flex;align-items:center;justify-content:center}
.team-blue{left:638px;top:2048px;width:14px;height:152px;background:var(--blue)}
.team-navy{left:1022px;top:2202px;width:65px;height:108px;background:var(--navy)}
.team-img{left:652px;top:1958px;width:404px;height:334px;border-radius:6px;background:linear-gradient(135deg,#dce9ef,#b4ccd6 50%,#8eacb9)}

/* applications */
.apps-head{left:0;top:2394px;width:1200px}
.apps-head h2{font-size:31px;margin-top:4px}
.app-card{top:2504px;height:306px;background:#fff;box-shadow:0 4px 18px rgba(0,0,0,.07);text-align:center}
.app-card .ph{height:174px}
.app-card h3{font-size:17px;font-weight:400;margin-top:36px}
.app-card p{font-size:12px;line-height:21px;color:var(--muted);margin:8px 14px 0}
.demo-btn{left:504px;top:2848px;width:176px;height:42px;background:var(--blue-2);color:#fff;font-size:13px;font-weight:500;display:flex;align-items:center;justify-content:center}

/* investment */
.invest{left:0;top:2967px;width:1200px;height:575px;background:linear-gradient(135deg,#1596db,#0a86cf 60%,#1b8fd5)}
.invest-head{left:0;top:3032px;width:1200px}
.invest-head .eyebrow{color:#fff}
.invest-head h2{color:#fff;font-size:31px;margin-top:8px}
.invest-head .dash span{background:#fff}
.inv-card{top:3146px;width:289px;height:226px;background:#fff;border-radius:4px;text-align:center;padding-top:28px}
.inv-card .ic{width:66px;height:66px;border-radius:50%;margin:0 auto;display:flex;align-items:center;justify-content:center}
.inv-card h3{font-size:14px;font-weight:500;margin-top:24px}
.inv-card p{font-size:11.5px;line-height:21px;color:var(--ink);margin:8px 36px 0}
.ghost{top:3422px;height:42px;border:1.5px solid rgba(255,255,255,.8);background:rgba(255,255,255,.12);color:#fff;font-size:13px;font-weight:500;display:flex;align-items:center;justify-content:center}

/* testimonials */
.testi-head{left:0;top:3620px;width:1200px}
.testi-head h2{font-size:31px;margin-top:4px}
.testi-img{left:137px;top:3742px;width:426px;height:280px;border-radius:8px;background:linear-gradient(135deg,#c9d3d9,#8ea0aa 60%,#5c6e78)}
.testi-card{left:403px;top:3775px;width:649px;height:214px;border-radius:12px;background:#fff;border:1px solid #bfe4f3;box-shadow:0 8px 28px rgba(0,100,150,.10);padding:28px 42px}
.stars{display:flex;gap:6px}
.testi-card p{font-size:12.5px;line-height:24px;color:var(--ink);margin-top:14px}
.person{display:flex;align-items:center;gap:14px;margin-top:14px}
.avatar{width:40px;height:40px;border-radius:50%;background:#b98e74}
.person b{display:block;font-size:12.5px;font-weight:500;color:var(--ink)}
.person span{font-size:12px;color:var(--muted)}
.arrow{left:1032px;width:30px;height:30px;border-radius:50%;background:#fff;box-shadow:0 2px 8px rgba(0,0,0,.12);display:flex;align-items:center;justify-content:center}

/* footer */
.footer{left:0;top:4111px;width:1200px;height:370px;background:var(--footer);color:#d6dde3}
.footer .brand{color:#fff}
.footer .brand-dot{background:#fff}
.f-col h4{color:#fff;font-size:15px;font-weight:500;margin-bottom:16px}
.f-col li{list-style:none;font-size:13px;line-height:29px}
.f-col li::before{content:"+";color:var(--blue-2);margin-right:8px}
.contact-row{display:flex;gap:18px;align-items:center;font-size:12.5px;line-height:22px;margin-bottom:22px}
.c-ic{width:32px;height:32px;border-radius:50%;flex:none;display:flex;align-items:center;justify-content:center}
.social{display:flex;gap:8px;align-items:center;font-size:12.5px}
.social i{width:22px;height:22px;border-radius:50%;border:1px solid #8a99a6;display:inline-block}
.social i.on{background:var(--blue-2);border-color:var(--blue-2)}
.legal{left:141px;top:4440px;width:912px;display:flex;justify-content:space-between;font-size:11px;color:#9aa6b0}
.legal u{color:#fff}
</style>
</head>
<body>

<!-- header + hero -->
<div class="abs hero-bg"></div>
<div class="abs hero-img" role="img" aria-label="Hand touching a digital healthcare interface with medical icons and a glowing cross"></div>
<header>
  <div class="abs brand" style="left:106px;top:38px"><span class="brand-dot"></span>VORENTbio</div>
  <nav class="abs nav"><span>Home</span><span>Our Services</span><span>About Us</span><span>Technology</span><span>Blog</span></nav>
  <div class="abs login">Login</div>
  <div class="abs contact-btn">Contact US</div>
</header>
<section class="hero">
  <h1 class="abs">Redefining T Cell Discovery For The Future Of Medicine</h1>
  <p class="abs">Introducing VORENT — a breakthrough platform to rapidly and affordably identify antigen-specific T cells for cancer, autoimmunity, and beyond.</p>
  <div class="abs hero-btns"><span class="pill pill-blue">Products</span><span class="pill pill-line">Plan a Demo</span></div>
  <div class="abs stats-bar">
    <div class="item"><span class="stat-num">40K</span>Happy Customer</div>
    <div class="item"><span class="stat-num">14+</span>Year of Experience</div>
    <div class="item"><span class="stat-num">99%</span>Success Rate</div>
  </div>
</section>

<!-- platform -->
<section>
  <div class="abs platform-head center"><div class="eyebrow">The VORENT Platform</div><h2>A Cutting Edge Solution For Identifying</h2></div>
  <div class="abs feature" style="left:141px;top:831px"><h3>Rapid</h3><p>Identify T cells in hours, not days, accelerating research and therapeutic development.</p></div>
  <div class="abs f-icon" style="left:186px;top:802px;background:var(--blue)"><svg width="26" height="26" viewBox="0 0 24 24" fill="none" stroke="#fff" stroke-width="1.6"><path d="M13 2 4 14h7l-1 8 9-12h-7z"/></svg></div>
  <div class="abs feature" style="left:459px;top:831px"><h3>Versatile</h3><p>Supports multiple cell types and applications, from cancer to autoimmune diseases.</p></div>
  <div class="abs f-icon" style="left:504px;top:802px;background:var(--teal)"><svg width="26" height="26" viewBox="0 0 24 24" fill="none" stroke="#fff" stroke-width="1.6"><circle cx="12" cy="8" r="3"/><path d="M3 17c3-2 6-2 9 0s6 2 9 0M6 20h12"/></svg></div>
  <div class="abs feature" style="left:779px;top:831px"><h3>Cost Effective</h3><p>Reduces resources needed, making immunotherapy more accessible.</p></div>
  <div class="abs f-icon" style="left:824px;top:802px;background:var(--blue)"><svg width="26" height="26" viewBox="0 0 24 24" fill="none" stroke="#fff" stroke-width="1.6"><circle cx="13" cy="8" r="5"/><path d="M13 5.5v5M2 19l5-3h6l4-2"/></svg></div>
</section>

<!-- about -->
<section>
  <div class="abs about-accent"></div>
  <div class="abs about-img ph" role="img" aria-label="Doctor working on a laptop with holographic medical icons"></div>
  <div class="abs badge" aria-hidden="true"></div>
  <div class="abs about-text">
    <div class="eyebrow">About Us</div>
    <h2>Global Research Partnerships</h2>
    <div class="dash"><span></span><span></span><span></span></div>
    <p>Lorem Ipsum is simply dummy text of the printing and typesetting industry. Lorem Ipsum has been the industry's standard dummy text ever since the 1500s, when an unknown printer took a galley of type and scrambled it to make a type specimen book. It has survived not only five centuries, but also the leap into electronic typesetting, remaining essentially unchanged</p>
    <p style="margin-top:10px">Various versions have evolved over the years, sometimes by accident, sometimes on purpose (injected humour and the like). There are many variations of passages.</p>
    <div style="display:flex;align-items:center;gap:20px;margin-top:18px"><span class="btn btn-blue" style="height:38px;padding:0 20px">Read More</span><span class="link-blue">Call To Our Team</span></div>
  </div>
</section>

<!-- stats band -->
<section>
  <div class="abs stats-band"></div>
  <div class="abs notch"></div>
  <svg class="abs cross" style="left:1101px;top:1561px" viewBox="0 0 80 80" fill="none" stroke="#fff" stroke-width="4"><path d="M32 4h16v28h28v16H48v28H32V48H4V32h28z" fill="var(--teal)"/></svg>
  <svg class="abs cross" style="left:52px;top:1818px" viewBox="0 0 80 80" fill="none" stroke="#fff" stroke-width="4"><path d="M32 4h16v28h28v16H48v28H32V48H4V32h28z" fill="var(--teal)"/></svg>
  <div class="abs band-stats">
    <div class="item"><div class="stat-num">40K</div><span>Happy Customer</span></div>
    <div class="item"><div class="stat-num">50+</div><span>Team Members</span></div>
    <div class="item"><div class="stat-num">14+</div><span>Year Of experience</span></div>
    <div class="item"><div class="stat-num">99%</div><span>Success Rate</span></div>
  </div>
</section>

<!-- team -->
<section>
  <div class="abs team-text">
    <div class="eyebrow">About VORENT</div>
    <h2>We are a team of innovators</h2>
    <div class="dash"><span></span><span></span><span></span></div>
    <p style="margin-top:14px">VORENT is committed to revolutionizing T cell therapy by making identification faster, more precise, and accessible, empowering researchers and clinicians to develop life-saving treatments.</p>
    <p>Our platform removes barriers in immunotherapy, enabling breakthroughs in cancer, autoimmune diseases, infectious diseases, and precision medicine.</p>
    <div style="display:flex;gap:18px;margin-top:20px">
      <span class="check"><i><svg width="11" height="11" viewBox="0 0 12 12" fill="none" stroke="#fff" stroke-width="2"><path d="M2 6l3 3 5-6"/></svg></i>Founded by Leading Immunologists</span>
      <span class="check"><i><svg width="11" height="11" viewBox="0 0 12 12" fill="none" stroke="#fff" stroke-width="2"><path d="M2 6l3 3 5-6"/></svg></i>Patented Proprietary</span>
    </div>
    <div style="margin-top:16px"><span class="check"><i><svg width="11" height="11" viewBox="0 0 12 12" fill="none" stroke="#fff" stroke-width="2"><path d="M2 6l3 3 5-6"/></svg></i>Global Research Partnerships</span></div>
  </div>
  <div class="abs team-blue"></div>
  <div class="abs team-navy"></div>
  <div class="abs team-img" role="img" aria-label="Group of smiling scientists in white lab coats"></div>
</section>

<!-- applications -->
<section>
  <div class="abs apps-head center"><div class="eyebrow">Applications</div><h2>Advancing immunotherapy across diverse diseases</h2><div class="dash"><span></span><span></span><span></span></div></div>
  <div class="abs app-card" style="left:0;width:266px"><div class="ph" role="img" aria-label="Hands holding a red awareness ribbon" style="background:linear-gradient(135deg,#e9edf0,#c8d2d8)"></div><h3>Cancer Immunotherapy</h3><p>Identify tumor-specific T cells for effective, low-side-effect therapies.</p></div>
  <div class="abs app-card" style="left:303px;width:273px"><div class="ph" role="img" aria-label="Doctor examining a patient's neck" style="background:linear-gradient(135deg,#dfe6ea,#a8b9c2)"></div><h3>Autoimmune Disease</h3><p>Target autoreactive T cells for precise autoimmune therapies.</p></div>
  <div class="abs app-card" style="left:610px;width:273px"><div class="ph" role="img" aria-label="Gloved hands holding a petri dish in a lab" style="background:linear-gradient(135deg,#d9e8f2,#8db6d4)"></div><h3>Infectious Disease</h3><p>Develop vaccines and treatments by identifying pathogen-specific T cells.</p></div>
  <div class="abs app-card" style="left:918px;width:275px"><div class="ph" role="img" aria-label="Laboratory microscope with sample slides" style="background:linear-gradient(135deg,#c5ccd2,#6e7c86)"></div><h3>Precision Medicine</h3><p>Enable tailored therapies by mapping patient-specific immune responses.</p></div>
  <div class="abs demo-btn">Request a Demo</div>
</section>

<!-- investment -->
<section>
  <div class="abs invest"></div>
  <div class="abs invest-head center"><div class="eyebrow">Investment Opportunity</div><h2>Join us to shape the future of immunotherapy</h2><div class="dash"><span></span><span></span><span></span></div></div>
  <div class="abs inv-card" style="left:141px"><div class="ic" style="background:var(--blue-pale)"><svg width="32" height="32" viewBox="0 0 24 24" fill="none" stroke="var(--blue)" stroke-width="1.8"><path d="M4 20V14M9 20V11M14 20V13M19 20V8M4 10l5-4 4 3 6-6"/></svg></div><h3>Market Potential</h3><p>The cell therapy market is set to reach $20B by 2028, with T cell therapies driving growth.</p></div>
  <div class="abs inv-card" style="left:456px"><div class="ic" style="background:var(--blue)"><svg width="30" height="30" viewBox="0 0 24 24" fill="none" stroke="#fff" stroke-width="1.8"><circle cx="12" cy="9" r="6"/><circle cx="12" cy="9" r="2.5"/><path d="M8 14l-2 7 6-3 6 3-2-7"/></svg></div><h3>Competitive Edge</h3><p>10x faster and 5x more cost-effective than existing methods, with broad applications.</p></div>
  <div class="abs inv-card" style="left:769px"><div class="ic" style="background:var(--blue-pale)"><svg width="30" height="30" viewBox="0 0 24 24" fill="none" stroke="var(--blue)" stroke-width="1.8"><path d="M10 14a4 4 0 0 1 0-6l3-3a4 4 0 0 1 6 6l-2 2M14 10a4 4 0 0 1 0 6l-3 3a4 4 0 0 1-6-6l2-2"/></svg></div><h3>IP Strength</h3><p>Robust portfolio with multiple patents protecting our core technology.</p></div>
  <div class="abs ghost" style="left:391px;width:212px">Connect with Our Team</div>
  <div class="abs ghost" style="left:619px;width:188px">Download Pitch Deck</div>
</section>

<!-- testimonials -->
<section>
  <div class="abs testi-head center"><div class="eyebrow">Testimonials</div><h2>What to say our client About us</h2><div class="dash"><span></span><span></span><span></span></div></div>
  <div class="abs testi-img" role="img" aria-label="Smiling professional woman with glasses at a cafe table"></div>
  <div class="abs testi-card">
    <div class="stars">
      <svg width="13" height="13" viewBox="0 0 24 24" fill="var(--star)"><path d="M12 2l3 7 7 .6-5.3 4.7 1.7 7.2L12 17.8 5.6 21.5l1.7-7.2L2 9.6 9 9z"/></svg>
      <svg width="13" height="13" viewBox="0 0 24 24" fill="var(--star)"><path d="M12 2l3 7 7 .6-5.3 4.7 1.7 7.2L12 17.8 5.6 21.5l1.7-7.2L2 9.6 9 9z"/></svg>
      <svg width="13" height="13" viewBox="0 0 24 24" fill="var(--star)"><path d="M12 2l3 7 7 .6-5.3 4.7 1.7 7.2L12 17.8 5.6 21.5l1.7-7.2L2 9.6 9 9z"/></svg>
      <svg width="13" height="13" viewBox="0 0 24 24" fill="var(--star)"><path d="M12 2l3 7 7 .6-5.3 4.7 1.7 7.2L12 17.8 5.6 21.5l1.7-7.2L2 9.6 9 9z"/></svg>
      <svg width="13" height="13" viewBox="0 0 24 24" fill="var(--star)"><path d="M12 2l3 7 7 .6-5.3 4.7 1.7 7.2L12 17.8 5.6 21.5l1.7-7.2L2 9.6 9 9z"/></svg>
    </div>
    <p>Lorem Ipsum Is Simply Dummy Text Of The Printing And Typesetting Industry. Lorem Ipsum Has Been The Industry's Standard Dummy Text Ever Since The 1500s, When An Unknown Printer Took A Galley</p>
    <div class="person"><div class="avatar" role="img" aria-label="Reviewer portrait"></div><div><b>Mara Ellison</b><span>Marketing Coordinator</span></div></div>
  </div>
  <div class="abs arrow" style="top:3849px"><svg width="12" height="12" viewBox="0 0 12 12" fill="none" stroke="var(--ink)" stroke-width="1.4"><path d="M1 6h10M7 2l4 4-4 4"/></svg></div>
  <div class="abs arrow" style="top:3889px"><svg width="12" height="12" viewBox="0 0 12 12" fill="none" stroke="var(--ink)" stroke-width="1.4"><path d="M11 6H1M5 2 1 6l4 4"/></svg></div>
</section>

<!-- footer -->
<footer>
  <div class="abs footer"></div>
  <div class="abs brand" style="left:143px;top:4183px"><span class="brand-dot"></span>VORENTbio</div>
  <p class="abs" style="left:143px;top:4232px;width:180px;font-size:12.5px;line-height:21px;color:#d6dde3">Lorem Ipsum is simply dummy text of the printing and typesetting industry.</p>
  <div class="abs social" style="left:143px;top:4332px;color:#d6dde3">Follow Us:<i></i><i class="on"></i><i></i></div>
  <div class="abs f-col" style="left:430px;top:4183px"><h4>Quick Links</h4><ul><li>Home</li><li>About Us</li><li>Technology</li><li>Blog</li><li>Contact</li></ul></div>
  <div class="abs f-col" style="left:609px;top:4183px"><h4>VORENT Platform</h4><ul><li>Rapid</li><li>Versatile</li><li>Unbiased</li><li>Cost-Effective</li></ul></div>
  <div class="abs f-col" style="left:823px;top:4183px;width:240px">
    <h4>Contact Us</h4>
    <div class="contact-row"><span class="c-ic" style="background:#2a3744"><svg width="14" height="14" viewBox="0 0 24 24" fill="none" stroke="#fff" stroke-width="2"><path d="M12 22s7-7 7-12a7 7 0 0 0-14 0c0 5 7 12 7 12z"/><circle cx="12" cy="10" r="2.5"/></svg></span><span>48 Harbor Science Way, Lindenport, MA 02190</span></div>
    <div class="contact-row"><span class="c-ic" style="background:var(--blue)"><svg width="14" height="14" viewBox="0 0 24 24" fill="#fff"><path d="M6.6 10.8a15 15 0 0 0 6.6 6.6l2.2-2.2a1 1 0 0 1 1-.25 11.4 11.4 0 0 0 3.6.57 1 1 0 0 1 1 1V20a1 1 0 0 1-1 1A17 17 0 0 1 3 4a1 1 0 0 1 1-1h3.5a1 1 0 0 1 1 1c0 1.25.2 2.45.57 3.6a1 1 0 0 1-.25 1z"/></svg></span><span>Phone: (555) 014-2290</span></div>
    <div class="contact-row"><span class="c-ic" style="background:#2a3744"><svg width="14" height="14" viewBox="0 0 24 24" fill="none" stroke="#fff" stroke-width="2"><rect x="3" y="5" width="18" height="14" rx="2"/><path d="M3 7l9 6 9-6"/></svg></span><span>hello@vorentbio.example</span></div>
  </div>
  <div class="abs legal"><span>VORENT Is A Registered Trademark. Patents Pending.</span><u>Privacy Policy | Terms Of Service</u></div>
</footer>

</body>
</html>
```